Corvanta512 Business Card Redesign

I want to create a design for brand new business cards, I need something exceptional for clear plastic business card design. Please do not submit without it being on a clear design. Photos of the various logo versions attached.

```html
<!DOCTYPE html>
<html lang="en">
<head>
<meta charset="utf-8">
<title>Corvanta512 Business Card</title>
<link href="https://fonts.googleapis.com/css2?family=Montserrat:wght@500;600;700;800&family=Cinzel:wght@600;700&display=swap" rel="stylesheet">
<style>
  :root {
    --bg: #121212;
    --plum-deep: #2f0c3c;
    --plum: #4a2154;
    --plum-light: #6e4c78;
    --gold: #e2b659;
    --gold-soft: #f0cf7f;
    --white: #ffffff;
  }
  * { margin: 0; padding: 0; box-sizing: border-box; }
  html, body { width: 1200px; height: 1019px; overflow: hidden; background: var(--bg); }
  body { position: relative; font-family: "Montserrat", sans-serif; }

  .card {
    position: absolute;
    left: 280px;
    width: 640px;
    height: 366px;
    border-radius: 28px;
    overflow: hidden;
    background: linear-gradient(160deg, var(--plum-light) 0%, var(--plum) 55%, #52295d 100%);
    box-shadow: 0 0 0 2px rgba(255,255,255,0.18) inset, 0 20px 40px rgba(0,0,0,0.5);
    opacity: 0.96;
  }
  .card-front { top: 90px; }
  .card-back { top: 536px; }
  .card-art { position: absolute; inset: 0; width: 100%; height: 100%; }

  /* front */
  .brand-block { position: absolute; left: 0; width: 270px; top: 166px; text-align: center; }
  .brand-name { font-weight: 800; font-size: 26px; letter-spacing: 1px; color: var(--gold); white-space: nowrap; }
  .brand-mark { display: inline-block; width: 12px; height: 12px; border-radius: 50%; background: var(--gold); margin-right: 8px; vertical-align: 3px; }

  .contact { position: absolute; left: 340px; top: 40px; color: var(--white); }
  .person-name { font-weight: 700; font-size: 38px; color: var(--gold); margin-bottom: 14px; white-space: nowrap; }
  .contact-line { display: flex; align-items: center; font-weight: 500; font-size: 17px; line-height: 28px; white-space: nowrap; }
  .contact-line svg { width: 20px; height: 20px; margin-right: 10px; }
  .contact-line.email { margin-top: 10px; }
  .response-note { font-weight: 700; font-size: 17px; color: var(--gold); margin-top: 10px; white-space: nowrap; }

  .consult-band {
    position: absolute; left: 340px; right: 0; top: 280px; height: 50px;
    background: var(--gold-soft); border-radius: 25px 0 0 25px;
    color: var(--plum-deep); font-weight: 800; font-size: 21px;
    display: flex; align-items: center; padding-left: 26px; white-space: nowrap;
  }

  /* back */
  .back-brand { position: absolute; top: 40px; left: 0; right: 0; text-align: center; }
  .back-brand .brand-name { font-size: 28px; }
  .services { position: absolute; top: 104px; left: 40px; right: 40px; display: flex; justify-content: space-between; }
  .service { width: 130px; text-align: center; }
  .service-icon { display: block; margin: 0 auto 10px; width: 46px; height: 46px; border-radius: 50%; background: var(--gold); }
  .service-label { font-family: "Cinzel", serif; font-weight: 700; font-size: 16px; color: var(--white); letter-spacing: 1px; }
  .website { position: absolute; left: 0; right: 0; top: 296px; text-align: center; color: var(--white); font-size: 18px; letter-spacing: 4px; }
  .website strong { color: var(--gold); font-weight: 700; }
</style>
</head>
<body>

<section class="card card-front" aria-label="Business card front">
  <svg class="card-art" viewBox="0 0 640 366" preserveAspectRatio="none" aria-hidden="true">
    <path d="M0 0 H272 C300 120 285 270 390 366 H0 Z" fill="#2f0c3c"/>
    <path d="M272 0 C300 120 285 270 390 366" fill="none" stroke="#e2b659" stroke-width="6"/>
  </svg>
  <div class="brand-block">
    <div class="brand-name"><span class="brand-mark"></span>CORVANTA512</div>
  </div>
  <div class="contact">
    <div class="person-name">Mara Ellison</div>
    <div class="contact-line">
      <svg viewBox="0 0 20 20"><circle cx="10" cy="10" r="10" fill="#e2b659"/><path d="M6.5 5.5l2 2-1 1.2a6 6 0 0 0 3.8 3.8l1.2-1 2 2-1.3 1.3C10 14.5 5.5 10 5.2 6.8z" fill="#4a2154"/></svg>
      (844) CRVA-512
    </div>
    <div class="contact-line">
      <svg viewBox="0 0 20 20"><circle cx="10" cy="10" r="10" fill="#e2b659"/><path d="M6.5 5.5l2 2-1 1.2a6 6 0 0 0 3.8 3.8l1.2-1 2 2-1.3 1.3C10 14.5 5.5 10 5.2 6.8z" fill="#4a2154"/></svg>
      1-844-2782-512
    </div>
    <div class="contact-line email">
      <svg viewBox="0 0 20 20"><circle cx="10" cy="10" r="10" fill="#e2b659"/><rect x="5" y="6.5" width="10" height="7" rx="1" fill="#4a2154"/><path d="M5.5 7l4.5 3.5L14.5 7" fill="none" stroke="#e2b659" stroke-width="1"/></svg>
      hello@corvanta512.com
    </div>
    <div class="response-note">We'll respond within 24 hours</div>
  </div>
  <div class="consult-band">24/7 Free Consultation</div>
</section>

<section class="card card-back" aria-label="Business card back">
  <svg class="card-art" viewBox="0 0 640 366" preserveAspectRatio="none" aria-hidden="true">
    <path d="M0 170 C160 230 360 230 470 250 C560 268 610 310 640 350 V366 H0 Z" fill="#2f0c3c"/>
    <path d="M0 170 C160 230 360 230 470 250 C560 268 610 310 640 350" fill="none" stroke="#e2b659" stroke-width="6"/>
  </svg>
  <div class="back-brand">
    <div class="brand-name"><span class="brand-mark"></span>CORVANTA512</div>
  </div>
  <div class="services">
    <div class="service"><span class="service-icon" role="img" aria-label="Gavel icon"></span><span class="service-label">LEGAL</span></div>
    <div class="service"><span class="service-icon" role="img" aria-label="Medical cross icon"></span><span class="service-label">MEDICAL</span></div>
    <div class="service"><span class="service-icon" role="img" aria-label="Raised fist icon"></span><span class="service-label">SUPPORT</span></div>
    <div class="service"><span class="service-icon" role="img" aria-label="Shield with tick icon"></span><span class="service-label">INSURANCE</span></div>
  </div>
  <div class="website">www.<strong>corvanta512</strong>.com</div>
</section>

</body>
</html>
```